依頼詳細
ニュースレターのリニューアルに伴う「ニュースレターのテンプレート」作成をお願いします。
下記の「最終成果物」と「必須掲載項目」を満たしていれば、デザインやレイアウトは問いません。お任せいたします。

【最終成果物】
納品は「InDesign」ファイルでお願いします。

サイズ:A4 中綴じ(左開き)横書き

希望する納品物は次の2点です。
1.表紙
2.見開き2ページ(表紙のあとのP2~P3)

下記、必須掲載項目のうち、2~9は納品後テキストや画像の変更を想定しています。
編集可能な状態で作成してください。

【必須掲載項目】
以下は「表紙」と「見開き2ページ」で必ず入れていただきたい項目と挿入するテキストになります。
各項目のデザイン、レイアウト(ページ数以外)はお任せいたします。

必須掲載項目は添付ファイル「必須掲載項目.pdf」にもまとめてあります。ご参照ください。

≪ 表紙 ≫
1. タイトル
挿入テキスト:Harbor insight Bulletin

2. サブタイトル
挿入テキスト:WEB起業家に送る、思考の実践情報。”キーワードをせいするもの、ネットを制す”

3. 号数
挿入テキスト:150号

4. 発行年月
挿入テキスト:2022年12月

5. 特集見出し
挿入テキスト:特集
※ サンプルでハイライトに該当する部分になります。
※ 見出しは2件掲載する予定です。テキストの分量はサンプルと同程度を想定してください。

6. 巻頭言タイトル
挿入テキスト:巻頭言

7. 筆者顔写真
挿入画像:ファイル「筆者写真.png」

8. ページ数(フッター)
挿入テキスト:該当ページ数 Harbor insight 号数(例:1 Harbor insight 150号)
※ レイアウトは左寄せにしてください。

≪見開き2ページ≫
9. ページ数(フッター)
挿入テキスト:該当ページ数 Harbor insight 号数(例:2 Harbor insight 150号)
※ 表紙のフッターからの連番になります。
※ 2ページ(右側ページ)は右寄せ、3ページ(左側ページ)は左寄せにレイアウトしてください。
記載項目
・色はコーポレートカラーの HI DEEP BLUE(RGB:R:0 G:0 B:192、#0000c0)をベースにHI RED PURPLE(RGB: R:230 G:0 B:255、#e600ff)を使用してください。
※ コーポレートカラーの詳細は添付ファイル「必須掲載項目.pdf」をご参照ください。

イメージ、配色などは弊社HPをご参照ください。
https://www.hbi-example.co.jp/

参考として弊社ロゴデータを添付いたします。ご参照ください(ファイル名:harborinsight_logo.zip)

・ニュースレターはデータと印刷両方で配布いたします。カラーで作成していただきたいですが、印刷時はモノクロになることを考慮したデザインにしていただければと思います。

・フォントは有料フォントは使用せず、Adobeでダウンロード可能なものをご使用ください。

・サンプルとして現在仕様しているテンプレートで作成したニュースレターを添付いたします。(ファイル名:Sample.pdf)
希望イメージ
シンプル 複雑
単色 カラフル
暗い 明るい
日常 高級
遊び心 厳粛
未来的 伝統的
女性的 男性的
希望する色
コーポレートカラーをベースに。カラーコードは添付を参照下さい
補足説明
最終納品はInDesign形式でお願いします。
依頼詳細の【必須掲載項目】のうち、8と9の記載内容に誤りがありましたので、
訂正させていただきます。大変失礼いたしました。

誤)
8. ページ数(フッター)
※ レイアウトは左寄せにしてください。

正)
8. ページ数(フッター)
※ レイアウトは右寄せにしてください。

誤)
9. ページ数(フッター)
※ 表紙のフッターからの連番になります。

正)
9. ページ数(フッター)
※ 表紙のフッターからの連番になります。
※ 2ページ(左側ページ)は左寄せ、3ページ(右側側ページ)は右寄せにレイアウトしてください。

(※ 添付の指示書も誤った内容となっています。お手数ですがこちらの訂正をご参照ください。)

既にご提案いただいている方のうち、当初の指示に従って作成していただいている方については、
再提案いただく必要はございません。
採用となった場合、修正の相談をさせていただければと思います。
■ 選んだ理由

コンセプトとこちらの希望をよくご理解いただき、イメージ通りのデザインだったため選ばせていただきました。

■ 提案者全員のお礼・コメント

このたびはご提案いただきありがとうございました。

皆さん弊社のHPを読み込んでくださったり、
コンセプト実現のためのアイデアをご提案いただいたり、
よいご提案ばかりで選ぶのにお時間をいただいてしまいました。

またデザイン関連で必要が生じたときはワークモールで公募したいと思います。
その際はぜひご応募いただければ幸いです。

```html
<!DOCTYPE html>
<html lang="ja">
<head>
<meta charset="utf-8">
<title>Harbor insight Bulletin vol.150</title>
<link href="https://fonts.googleapis.com/css2?family=Noto+Sans+JP:wght@400;500;700;900&family=Montserrat:ital,wght@0,600;0,800;1,700;1,800&display=swap" rel="stylesheet">
<style>
  :root{
    --deep-blue:#0000c0;
    --red-purple:#e600ff;
    --ink:#222233;
    --muted:#5a5a7a;
    --photo:#b9b4ae;
    --paper:#ffffff;
  }
  *{margin:0;padding:0;box-sizing:border-box}
  html,body{width:846px;height:1200px;overflow:hidden;background:var(--paper)}
  body{font-family:"Noto Sans JP",sans-serif;color:var(--ink);position:relative}
  .tagline{position:absolute;left:28px;top:12px;font-family:"Montserrat",sans-serif;font-size:10.5px;font-weight:600;color:var(--muted);line-height:1.35}
  .subtitle{position:absolute;left:28px;top:46px;font-size:16px;font-weight:700;color:var(--ink);line-height:1.45}
  .brand{position:absolute;right:28px;top:22px;width:190px;text-align:center}
  .brand-mark{width:46px;height:46px;background:var(--red-purple);margin:0 auto 10px}
  .brand-name{font-size:22px;font-weight:700;color:var(--deep-blue);line-height:1.1}
  .spotlight{position:absolute;left:28px;top:132px;background:var(--red-purple);color:#fff;font-family:"Montserrat",sans-serif;font-style:italic;font-weight:800;font-size:20px;padding:3px 14px;box-shadow:4px 4px 0 var(--deep-blue)}
  .features{position:absolute;left:28px;top:168px;width:540px;height:140px;border:2px solid var(--red-purple);padding:14px 18px;font-weight:700;font-size:17px;line-height:1.55;color:var(--deep-blue)}
  .features p{margin-bottom:6px}
  .features mark{background:linear-gradient(transparent 60%,#f7c6ff 60%);color:inherit}
  .masthead{position:absolute;right:28px;top:170px;text-align:right;font-family:"Montserrat",sans-serif;font-style:italic;font-weight:800;line-height:.95}
  .masthead .news{font-size:62px;color:var(--deep-blue)}
  .masthead .letter{font-size:50px;color:var(--red-purple)}
  .masthead .issue{font-size:26px;color:var(--deep-blue);margin-top:14px}
  .masthead .issue b{font-size:44px}
  .masthead .date{font-size:16px;color:var(--deep-blue);margin-top:4px}
  .section-head{position:absolute;left:28px;top:336px;width:570px;border-bottom:2px solid var(--deep-blue)}
  .section-head span{display:inline-block;background:var(--deep-blue);color:#fff;font-size:20px;font-weight:700;padding:6px 28px;letter-spacing:.2em}
  .author{position:absolute;left:300px;top:408px;width:300px;text-align:right;font-size:11.5px;line-height:1.6}
  .author .name{font-size:19px;font-weight:700;margin-top:4px}
  .author .name small{font-family:"Montserrat",sans-serif;font-size:11px;font-style:italic;color:var(--muted);margin-left:8px}
  .photo{position:absolute;left:620px;top:385px;width:190px;height:140px;background:linear-gradient(135deg,#d8d4cf,var(--photo))}
  .body-copy{position:absolute;left:28px;top:548px;width:790px;font-size:12.5px;line-height:1.8;text-align:justify}
  .body-copy p{text-indent:1em;margin-bottom:4px}
  .placeholder{position:absolute;left:28px;top:960px;width:790px;font-size:13px;line-height:1.9;letter-spacing:.1em;color:var(--muted);overflow:hidden;white-space:nowrap}
  .continued{position:absolute;right:0;top:1124px;width:300px;height:42px;background:var(--deep-blue);color:#fff;font-family:"Montserrat",sans-serif;font-style:italic;font-weight:700;font-size:18px;display:flex;align-items:center;padding-left:22px;border-left:8px solid var(--red-purple)}
  .folio{position:absolute;right:28px;bottom:10px;font-family:"Montserrat",sans-serif;font-size:14px;font-weight:600;color:var(--deep-blue)}
</style>
</head>
<body>
  <div class="tagline">The highest practice information presented to a WEB entrepreneur.<br>The thing and network which control a keyword are "controlled." WEB</div>
  <div class="subtitle">起業家に贈る、最高の実践情報。<br>“キーワードを制するもの、ネットを制す”</div>

  <div class="brand">
    <div class="brand-mark"></div>
    <div class="brand-name">Harbor insight</div>
  </div>

  <div class="spotlight">SPOTLIGHT</div>
  <div class="features">
    <p>①新人・未経験を半年で１人前にする<br><mark>「手作り研修」の絶大な効果</mark></p>
    <p>②なぜ集客が失敗するのか？<br><mark>検索連動型広告だけではない！集客で成功する思考と戦略</mark></p>
  </div>

  <div class="masthead">
    <div class="news">NEWS</div>
    <div class="letter">LETTER</div>
    <div class="issue">vol.<b>150</b></div>
    <div class="date">Dec.2022</div>
  </div>

  <div class="section-head"><span>巻頭言</span></div>
  <div class="author">
    <div>株式会社 ハーバーインサイト</div>
    <div>代表取締役／広告事業部長</div>
    <div class="name">三崎 秀典<small>Hidenori Misaki</small></div>
  </div>
  <div class="photo" role="img" aria-label="筆者顔写真"></div>

  <div class="body-copy">
    <p>ハーバーインサイト　三崎です。</p>
    <p>さて、2019年も早くも春を迎えました。私たちハーバーインサイトもいよいよ人員が50名を突破しそうで、8月はじめに外部研修のオフィスから徒歩2〜3分の新拠点に引っ越しをいたしました。</p>
    <p>引っ越しの理由はもちろん、人員を来期70名、将来的には100名体制にするためのスペース確保です。それ以外にも、休憩スペースや会議室を増やし、また周囲の環境を細かく少しでも仕事しやすい場所にしようと、現在のオフィス環境を一新するような場所へ向けて引っ越しをしたかったためです。</p>
    <p>それにしても8年前に入居した時の頃は、時代の流れが感じられます。「すべての経営は設定価値の方向へ向かう」という言葉は打ち合わせのたびに思い出す言葉です。身の引き締まる思いです。</p>
    <p>会員の皆様にはよりよいサービスを提供できるよう、社員一丸になって精進致します！</p>
    <p>もちろんそのイニシャルも大変重要、デザインイメージはこんな感じ。天井高が2.5mと以前より開放感があり、セミナーは最適な立地で実施できるのを楽しみにしています。</p>
    <p>入居するビルのエレベーターホールも、かなりシンプルです。日比谷線駅から徒歩3分、有楽町線駅直結から5分。本格的に整備されて発信の中心地となり、2方向から集客に最適なビルです。</p>
  </div>

  <div class="placeholder">
    □□□□□□□□□□□□□□□□□□□□□□□□□□□□□□□□□□□□□□□□□□□□□□□□□□□<br>
    □□□□□□□□□□□□□□□□□□□□□□□□□□□□□□□□□□□□□□□□□□□□□□□□□□□<br>
    □□□□□□□□□□□□□□□□□□□□□□□□□□□□□□□□□□□□□□□□□□□□□□□□□□□<br>
    □□□□□□□□□□□□□□□□□□□□□□□□□□□□□□□□□□□□□□□□□□□□□□□□□□□<br>
    □□□□□□□□□□□□□□□□□□□□□□□□□□□□□□□□□□□□□□□□□□□□
  </div>

  <div class="continued">continued on the NextPage</div>
  <div class="folio">1</div>
</body>
</html>
```